Brandomir tile letterhead contractor

I would like to get a very good expressive letterhead or resume with great 3D design as a tile contractor company offering my services to others tile companies, general contractors and home owners clients. (This is the idea)
Founder/owner.
“Proud to represent and provide my life’s passion services as brandomir tile.”
I’m journeyman setter, I have passion for creating visually stunning designs with a focus on creativity usability. I have been working as setter with a remarkable companies for over 20 years and I specialize in commercial and residential projects.
My experience and expertise have enabled me to create beautiful master pieces for a wide range of clients, from a small businesses to a large corporations.
My first goal in any project that you hire me for is to provide a professional and high-quality product that meets and exceeds your expectations. You can really assured that I will strive tirelessly to produce the best results for our clients until the final project is done.
*My team will move forward with your needs in every step we walk together
*We have a very solid foundations knowledge altogether rely in the best equipment possible to make (builds)what it takes with best quality possible
*I’m an independent contractor and beaten to another prestigious companies …. ETC. ETC.
ILL TRY TO KEEP UPDATING MORE INFO.
Target Market(s)
General contractors, tile companies and home owners builders
Industry/Entity Type
Tile construction
Look and feel

```html
<!DOCTYPE html>
<html lang="en">
<head>
<meta charset="utf-8">
<title>Brandomir Tile Letterhead</title>
<link href="https://fonts.googleapis.com/css2?family=Open+Sans:wght@400&family=Source+Sans+3:wght@400;600&display=swap" rel="stylesheet">
<style>
:root{
  --brown:#55383a;
  --ink:#555555;
  --ink-soft:#5e5e5e;
  --paper:#ffffff;
  --backdrop:#e3e3e3;
  --sig:#e9e2e2;
}
*{margin:0;padding:0;box-sizing:border-box}
html,body{width:1200px;height:1141px;overflow:hidden;background:var(--backdrop)}
.letterhead{
  position:absolute;left:207px;top:20px;width:785px;height:1100px;
  background:var(--paper);box-shadow:0 3px 10px rgba(0,0,0,.25);
  font-family:"Source Sans 3",sans-serif;color:var(--ink);
}
.brand{position:absolute;left:56px;top:112px}
.brand-name{
  font-family:"Source Sans 3",sans-serif;font-weight:600;font-size:22px;
  color:var(--brown);display:flex;align-items:center;gap:8px
}
.brand-mark{width:12px;height:12px;background:var(--brown)}
.contact{position:absolute;right:56px;top:62px;list-style:none;text-align:right;
  font-family:"Open Sans",sans-serif;font-size:13px;color:var(--ink-soft)}
.contact li{height:19.6px;display:flex;justify-content:flex-end;align-items:center;gap:7px}
.contact svg{width:11px;height:11px;fill:var(--brown)}
.recipient{position:absolute;left:56px;top:314px}
.recipient-name{font-size:15px;text-transform:uppercase;color:var(--ink)}
.recipient-line{font-size:11.5px;line-height:19.4px}
.body{position:absolute;left:56px;top:411px;width:673px;font-size:12px;line-height:19.1px;text-align:justify;color:var(--ink-soft)}
.body p+p{margin-top:16.5px}
.closing{position:absolute;left:56px;top:716px;font-size:12.5px}
.signature{position:absolute;left:56px;top:746px;width:140px;height:26px;background:var(--sig);border-radius:3px}
.signer{position:absolute;left:56px;top:782px;font-size:15px}
.footer-band{
  position:absolute;left:0;top:1054px;width:785px;height:30px;background:var(--brown);
  display:flex;justify-content:space-between;align-items:center;padding:0 55px;
  font-family:"Open Sans",sans-serif;font-size:13px;color:#fff;text-transform:uppercase
}
</style>
</head>
<body>
<article class="letterhead">
  <header class="brand">
    <div class="brand-name"><span class="brand-mark"></span>Brandomir Tile</div>
  </header>

  <ul class="contact">
    <li>(555) 214-7730 <svg viewBox="0 0 24 24"><path d="M6.6 10.8a15.2 15.2 0 0 0 6.6 6.6l2.2-2.2a1 1 0 0 1 1-.25 11.4 11.4 0 0 0 3.6.57 1 1 0 0 1 1 1V20a1 1 0 0 1-1 1A17 17 0 0 1 3 4a1 1 0 0 1 1-1h3.5a1 1 0 0 1 1 1c0 1.250.2 2.45.57 3.57a1 1 0 0 1-.25 1z"/></svg></li>
    <li>brandomir.tile@mailbox.test <svg viewBox="0 0 24 24"><path d="M2 5h20v2l-10 6L2 7z"/><path d="M2 9.3l10 6 10-6V19H2z"/></svg></li>
    <li>Cedar Hollow Utah, 84000 <svg viewBox="0 0 24 24"><path d="M12 2a7 7 0 0 0-7 7c0 5.2 7 13 7 13s7-7.8 7-13a7 7 0 0 0-7-7zm0 9.5A2.5 2.5 0 1 1 12 6.5a2.5 2.5 0 0 1 0 5z"/></svg></li>
    <li>www.social.test/Brandomirti <svg viewBox="0 0 24 24"><rect x="3" y="3" width="18" height="18" rx="2"/></svg></li>
  </ul>

  <section class="recipient">
    <div class="recipient-name">Darren Holloway</div>
    <div class="recipient-line">President / CEO</div>
    <div class="recipient-line">City/State, Zip Code</div>
  </section>

  <section class="body">
    <p>Lorem Ipsum is simply dummy text of the printing and typesetting industry. Lorem Ipsum has been the industry's standard dummy text ever since the 1500s, when an unknown printer took a galley of type and scrambled it to make a type specimen book. It has survived not only five centuries, but also the leap into electronic typesetting, remaining essentially unchanged. It was popularised in the 1960s with the release of dry transfer sheets containing Lorem Ipsum passages, and more recently with desktop publishing software like page layout tools including versions of Lorem Ipsum.</p>
    <p>It is a long established fact that a reader will be distracted by the readable content of a page when looking at its layout. The point of using Lorem Ipsum is that it has a more-or-less normal distribution of letters, as opposed to using 'Content here, content here', making it look like readable English. Many desktop publishing packages and web page editors now use Lorem Ipsum as their default model text, and a searchaccident, sometimes on purpose (injected humour and the like).</p>
    <p>There are many variations of passages of Lorem Ipsum available, but the majority have suffered alteration in some form, by injected humour, or randomised words which don't look even slightly believable. If you are going to use a passage of Lorem Ipsum, you need to be sure there isn't anything embarrassing hidden in the middle of text.</p>
  </section>

  <div class="closing">Sincerely,</div>
  <div class="signature" role="img" aria-label="Handwritten signature of Laura Penner"></div>
  <div class="signer">Laura Penner</div>

  <footer class="footer-band">
    <span>20+Years Experience</span>
    <span>Free Estimates</span>
    <span>Licensed and Insured</span>
  </footer>
</article>
</body>
</html>
```